Rock, Paper Scissors Championship Flyer

We need a dynamic, bold and exciting flyer to promote the following event at our sports center. The event will be primarily focused for adults, but children are welcome to join

Rock, Paper, Scissors Championship - $$$ prizes
Date: June 9th, 2018
Time: 11am-4pm
Fee: $2 to enter, free for spectators
Heats to determine the overall ‘Rock, Paper, Scissors’ champion!
- Cash prizes on offer
- Live music.
- Food and beverage available for purchase

Belmoray Sports Center, Roselle NJ
908-555-0163
www.belmoraypark.example

Must include our logo (does not have to be huge) and County seal (both attached)

Colors

Designer to choose colors to be used in the design.

Requirements
Must have
• Should be fun and colorful
• The following info and attached logos:
• Rock, Paper, Scissors Championship - $$$ prizes
• Date: June 9th, 2018
• Time: 11am-4pm
• Fee: $2 to enter, free for spectators
• Heats to determine the overall ‘Rock, Paper, Scissors’ champion!
• - Cash prizes on offer
• - Live music.
• - Food and beverage available for purchase
• Belmoray Sports Center, Roselle NJ
• 908-555-0163
• www.belmoraypark.example
Nice to have
• There are a few inspirational photos attached to give an idea of what we are looking for.

```html
<!DOCTYPE html>
<html lang="en">
<head>
<meta charset="utf-8">
<title>Rock Paper Scissors Championship</title>
<link rel="stylesheet" href="https://fonts.googleapis.com/css2?family=Arimo:wght@700&family=Luckiest+Guy&family=Bungee&display=swap">
<style>
  :root {
    --ink: #05060d;
    --navy: #1a1f45;
    --magenta: #e60fd8;
    --violet: #8a2be2;
    --teal: #1fa6a6;
    --gold: #c9a227;
    --white: #ffffff;
    --skin: #f6ccc0;
  }
  html, body { margin: 0; padding: 0; overflow: hidden; background: var(--ink); }
  .flyer {
    position: relative; width: 927px; height: 1200px; overflow: hidden;
    background: radial-gradient(ellipse at 40% 45%, #2a3060 0%, var(--navy) 30%, var(--ink) 75%);
    font-family: "Arimo", Arial, sans-serif; color: var(--white);
  }
  .backdrop { position: absolute; inset: 0; }
  .event-meta { position: absolute; top: 14px; font-size: 35px; line-height: 40px; font-weight: 700; }
  .event-meta--left { left: 22px; }
  .event-meta--right { right: 22px; text-align: right; }
  .title-arch { position: absolute; left: 0; top: 0; }
  .title {
    position: absolute; left: 40px; width: 847px; top: 290px; margin: 0; text-align: center;
    white-space: nowrap;
    font-family: "Luckiest Guy", "Bungee", sans-serif; font-weight: 400; font-size: 58px; letter-spacing: 0;
    color: var(--white); -webkit-text-stroke: 5px #000; paint-order: stroke fill; line-height: 1;
    transform: scaleY(1.9);
  }
  .subtitle {
    position: absolute; left: 0; width: 927px; top: 418px; text-align: center; white-space: nowrap;
    font-family: "Bungee", sans-serif; font-size: 74px; line-height: 1; letter-spacing: 1px;
    color: var(--white); -webkit-text-stroke: 6px var(--magenta); paint-order: stroke fill;
  }
  .gesture {
    position: absolute; top: 494px; width: 160px; height: 160px; border-radius: 50%;
    background: var(--white); border: 7px solid var(--magenta); overflow: hidden;
  }
  .gesture__art { position: absolute; inset: 22px; border-radius: 50%;
    background: radial-gradient(circle at 50% 50%, var(--skin) 55%, #f1d9d2 100%); }
  .gesture--rock { left: 127px; }
  .gesture--paper { left: 371px; }
  .gesture--scissors { left: 611px; }
  .prizes {
    position: absolute; left: 0; width: 927px; top: 686px; text-align: center;
    font-size: 88px; line-height: 1; font-weight: 700; letter-spacing: 1px;
  }
  .heats {
    position: absolute; left: 0; width: 927px; top: 784px; margin: 0; text-align: center;
    font-size: 32px; line-height: 37px; font-weight: 700;
  }
  .highlights { position: absolute; left: 0; width: 927px; top: 926px; margin: 0; padding: 0;
    list-style: none; text-align: center; font-size: 40px; line-height: 52px; font-weight: 700; white-space: nowrap; }
  .highlights li { display: inline; }
  .highlights li::before { content: "•"; }
  .highlights .gap { margin-right: 36px; }
  .venue { position: absolute; left: 22px; top: 1074px; font-size: 30px; line-height: 38px; font-weight: 700; }
  .badge {
    position: absolute; top: 1052px; width: 136px; height: 136px; border-radius: 50%;
    background: var(--white); border: 6px solid var(--magenta); box-sizing: border-box;
    display: flex; align-items: center; justify-content: center; text-align: center;
  }
  .badge--center { left: 632px; }
  .badge--county { left: 780px; }
  .badge__name { font-size: 17px; line-height: 20px; font-weight: 700; color: var(--navy); padding: 0 10px; }
  .badge__seal { width: 98px; height: 98px; border-radius: 50%; background: #9a3b4a; }
</style>
</head>
<body>
<div class="flyer">
  <svg class="backdrop" width="927" height="1200" viewBox="0 0 927 1200" aria-hidden="true">
    <g fill="none" stroke-width="5">
      <polyline points="-20,560 150,430 320,600 40,1000" stroke="var(--magenta)" />
      <polyline points="927,380 760,480 900,760" stroke="var(--magenta)" />
      <polyline points="60,200 230,90 420,260" stroke="var(--violet)" />
      <polygon points="129,678 464,386 798,678 464,961" stroke="var(--teal)" stroke-width="6" />
      <rect x="129" y="670" width="618" height="231" stroke="var(--teal)" stroke-width="5" />
      <line x1="0" y1="640" x2="927" y2="690" stroke="var(--gold)" stroke-width="2" />
      <line x1="560" y1="1030" x2="927" y2="880" stroke="var(--teal)" stroke-width="3" />
    </g>
    <polygon points="240,120 300,110 270,165" fill="var(--teal)" />
    <polygon points="870,70 927,40 927,120" fill="var(--magenta)" />
    <polygon points="0,780 90,820 0,870" fill="var(--teal)" />
    <polygon points="820,500 927,470 927,540" fill="var(--gold)" />
    <polygon points="150,960 230,1000 170,1040" fill="var(--violet)" />
    <circle cx="300" cy="1000" r="40" fill="var(--gold)" opacity=".6" />
    <polygon points="0,1040 140,1000 60,1080" fill="var(--magenta)" opacity=".8" />
  </svg>

  <svg class="title-arch" width="927" height="520" viewBox="0 0 927 520" aria-hidden="true">
    <path d="M74,400 L74,290 Q110,170 464,165 Q817,170 853,290 L853,400" fill="none" stroke="var(--magenta)" stroke-width="8" />
    <line x1="60" y1="405" x2="867" y2="405" stroke="var(--magenta)" stroke-width="8" />
  </svg>

  <div class="event-meta event-meta--left">Date: June 9th, 2018<br>Time: 11am-4pm</div>
  <div class="event-meta event-meta--right">Fee: $2 to enter<br>Free for spectators</div>

  <h1 class="title">ROCK·PAPER·SCISSORS</h1>
  <div class="subtitle">CHAMPIONSHIP</div>

  <div class="gesture gesture--rock"><div class="gesture__art" role="img" aria-label="Illustrated hand making a rock fist"></div></div>
  <div class="gesture gesture--paper"><div class="gesture__art" role="img" aria-label="Illustrated flat open hand showing paper"></div></div>
  <div class="gesture gesture--scissors"><div class="gesture__art" role="img" aria-label="Illustrated hand making scissors with two fingers"></div></div>

  <div class="prizes">$$$ PRIZES</div>
  <p class="heats">Heats to determine the overall<br>‘Rock, Paper, Scissors’<br>champion!</p>

  <ul class="highlights">
    <li class="gap">Live music</li><li>Cash prizes on offer</li><br>
    <li>Food and beverage available for purchase</li>
  </ul>

  <div class="venue">Belmoray Sports Center, Roselle NJ<br>908-555-0163<br>www.belmoraypark.example</div>

  <div class="badge badge--center"><span class="badge__name">Belmoray Sports Center</span></div>
  <div class="badge badge--county"><span class="badge__seal" role="img" aria-label="County seal"></span></div>
</div>
</body>
</html>
```